Purchasing community for life science startups needs landing page for collecting of contact adresses

We are the "Vessel Alliance", the first purchasing community for life science startups. The idea is to bundle the needs of several smaller companies (laboratories) and to buy lab consumables and chemicals in larger quantities. This bargaining position, at the end of all participants can buy their products very low prices. In the attached powerpoint file you will find an idea and some elements, which demonstrate a little the style, which came into my mind.
Target Market(s)
Our target customers are startups and smaller biotech companies, which are too small to get the best prices. The aim of this landing page is to collect all interested parties.
Look and feel
Each slider illustrates characteristics of the customer's brand and the style your logo design should communicate.

```html
<!DOCTYPE html>
<html lang="de">
<head>
<meta charset="utf-8">
<title>Vessel Alliance – Gemeinsam einkaufen</title>
<link rel="stylesheet" href="https://fonts.googleapis.com/css2?family=Montserrat:wght@400;500;600;700&display=swap">
<style>
:root{
  --blue:#0e9bdc;
  --blue-deep:#0a5fa8;
  --navy:#0b3a6c;
  --ink:#111111;
  --text:#555a60;
  --muted:#8a8f95;
  --line:#e3e6ea;
  --field:#f6f7f8;
  --page:#f7f8f9;
  --white:#ffffff;
}
*{box-sizing:border-box;margin:0;padding:0}
html,body{width:1200px;height:2740px;overflow:hidden}
body{position:relative;background:var(--page);font-family:"Montserrat",Arial,sans-serif;color:var(--ink)}
.abs{position:absolute}
.hero-visual{left:0;top:0;width:1200px;height:493px;background:linear-gradient(100deg,#f2f5f8 0%,#dfe7ee 45%,#b9c8d6 75%,#cfd9e2 100%)}
.hero-white{left:0;top:493px;width:1200px;height:411px;background:var(--white)}
.header{left:131px;top:29px;width:938px;height:77px;background:var(--white);box-shadow:0 3px 12px rgba(0,0,0,.08);display:flex;align-items:center;padding:0 24px}
.brand{display:flex;align-items:center;gap:12px;font-weight:700;font-size:22px;color:var(--navy)}
.brand-square{width:38px;height:38px;background:var(--blue-deep)}
.contact{margin-left:auto;display:flex;align-items:center;gap:10px;font-size:14px;font-weight:700}
.contact .or{color:var(--blue);margin:0 14px}
.btn{background:var(--blue);color:var(--white);font-weight:700;font-size:13px;border:none;display:inline-flex;align-items:center;justify-content:center}
.header .btn{width:140px;height:38px}
.hero-title{left:131px;top:296px;font-size:35px;line-height:49px;font-weight:700}
.card{background:var(--white);box-shadow:0 4px 16px rgba(0,0,0,.08);display:flex;flex-direction:column;align-items:center;text-align:center;border-radius:3px}
.card .hex{margin-top:34px;width:84px;height:94px}
.card p{margin-top:16px;font-size:14.5px;line-height:23px;padding:0 20px;color:var(--ink);white-space:nowrap}
.promo{left:131px;top:760px;width:938px;height:104px;background:var(--white);box-shadow:0 4px 16px rgba(0,0,0,.07);display:flex;align-items:center;justify-content:center;text-align:center;font-size:22px;line-height:34px}
.promo strong{color:var(--blue)}
.band{left:0;top:900px;width:1200px;height:520px}
.section-title{width:1200px;text-align:center;font-weight:700}
.vorteile{top:995px;color:var(--white);font-size:33px}
.interest{top:1455px;font-size:34px}
.lead{top:1510px;width:1200px;text-align:center;color:var(--blue);font-size:16.5px}
.intro{left:0;top:1554px;width:1200px;text-align:center;color:var(--text);font-size:14.5px;line-height:22px;white-space:nowrap}
.form-card{left:378px;top:1659px;width:444px;height:338px;background:var(--white);box-shadow:0 4px 18px rgba(0,0,0,.08)}
.field{position:absolute;left:73px;width:298px;height:40px;background:var(--field);border:1px solid #eceef0;font-size:13px;color:#a0a4a9;padding:12px 13px;font-family:inherit}
.field.active{background:var(--white);border:1.5px solid #555;color:var(--ink)}
.form-card .btn{position:absolute;left:154px;top:270px;width:138px;height:39px}
.about{left:0;top:2030px;width:1200px;height:560px}
.microscope{left:174px;top:2120px;width:256px;height:405px;background:radial-gradient(ellipse at 50% 45%,#ffffff 0%,#e4e8ed 60%,#cfd5dc 100%);border-radius:40px 40px 12px 12px}
.feature{left:479px;width:560px;display:flex;gap:24px}
.feature svg{flex:none}
.feature p{font-size:14.3px;line-height:22px;color:var(--text)}
.feature b{color:var(--blue);font-weight:700}
.footer{left:0;top:2550px;width:1200px;height:190px}
.footer-text{top:2646px;width:1200px;text-align:center;color:#dfe7f0;font-size:14px;line-height:24px}
</style>
</head>
<body>

<div class="abs hero-visual" role="img" aria-label="Forscher im Laborkittel berührt ein leuchtendes Netz aus Labor- und Medizin-Symbolen"></div>
<div class="abs hero-white"></div>

<header class="abs header">
  <div class="brand"><span class="brand-square"></span>Vessel Alliance</div>
  <div class="contact">
    <svg width="20" height="20" viewBox="0 0 24 24" fill="none" stroke="#111" stroke-width="1.8"><path d="M5 3h4l2 5-3 2a11 11 0 0 0 6 6l2-3 5 2v4a2 2 0 0 1-2 2A17 17 0 0 1 3 5a2 2 0 0 1 2-2z"/></svg>
    <span>CALL : +123 456 7890</span><span class="or">OR</span>
    <span class="btn">ENQUIRE US</span>
  </div>
</header>

<h1 class="abs hero-title">Gemeinsam<br>einkaufen zu<br>Großhandelspreisen</h1>

<svg width="0" height="0" style="position:absolute">
  <defs>
    <linearGradient id="hexGrad" x1="0" y1="0" x2="0" y2="1">
      <stop offset="0" stop-color="#14a8e6"/><stop offset="1" stop-color="#0a5ea6"/>
    </linearGradient>
    <symbol id="hexShape" viewBox="0 0 84 94"><path d="M42 2l38 21v48L42 92 4 71V23z" fill="url(#hexGrad)"/></symbol>
  </defs>
</svg>

<div class="abs card" style="left:133px;top:484px;width:283px;height:234px">
  <svg class="hex" viewBox="0 0 84 94"><use href="#hexShape"/><g fill="none" stroke="#fff" stroke-width="2"><path d="M30 66h26M34 60h16M40 30l8 4-8 16-8-4z"/><path d="M46 44a12 12 0 0 1-4 16"/></g></svg>
  <p>Betreibst du ein<br>LifeScience Labor?</p>
</div>
<div class="abs card" style="left:458px;top:484px;width:284px;height:234px">
  <svg class="hex" viewBox="0 0 84 94"><use href="#hexShape"/><g fill="none" stroke="#fff" stroke-width="2"><rect x="31" y="28" width="8" height="36" rx="4"/><rect x="45" y="28" width="8" height="36" rx="4"/><path d="M31 46h8M45 50h8"/></g></svg>
  <p>Benötigst du regelmäßig<br>Chemikalien, Laborglas und<br>Verbrauchsmaterialien?</p>
</div>
<div class="abs card" style="left:785px;top:484px;width:284px;height:234px">
  <svg class="hex" viewBox="0 0 84 94"><use href="#hexShape"/><g fill="none" stroke="#fff" stroke-width="2"><path d="M30 48l18-18h10v10L40 58z"/><circle cx="52" cy="36" r="2"/><path d="M38 46l6 6M42 42l3 3"/></g></svg>
  <p>Sind deine Abnahmemengen<br>zu klein, um maximale<br>Rabatte zu erhalten?</p>
</div>

<div class="abs promo"><p>hen take part in the first lab campaign 2019 and<br>Save up to <strong>40%</strong> on purchases.</p></div>

<svg class="abs band" viewBox="0 0 1200 520" role="img" aria-label="Laborglas und Mikroskop in blauem Licht">
  <defs>
    <linearGradient id="bandGrad" x1="0" y1="0" x2="1" y2="1">
      <stop offset="0" stop-color="#2f7fc6"/><stop offset=".5" stop-color="#5d9fd6"/><stop offset="1" stop-color="#9bc3e4"/>
    </linearGradient>
  </defs>
  <polygon points="0,4 1200,80 1200,516 0,420" fill="url(#bandGrad)"/>
  <polygon points="620,44 1200,80 1200,260" fill="#1e8fd8" opacity=".55"/>
</svg>

<h2 class="abs section-title vorteile">Vorteile</h2>

<div class="abs card" style="left:133px;top:1069px;width:283px;height:217px">
  <svg class="hex" viewBox="0 0 84 94"><use href="#hexShape"/><g fill="none" stroke="#fff" stroke-width="2"><path d="M26 34h6l5 22h20l4-14H34"/><circle cx="40" cy="62" r="2.5"/><circle cx="54" cy="62" r="2.5"/><path d="M47 40v8M43 44h8"/></g></svg>
  <p style="font-size:14px">Kaufe ein zu Großhandelspreisen</p>
</div>
<div class="abs card" style="left:458px;top:1069px;width:284px;height:217px">
  <svg class="hex" viewBox="0 0 84 94"><use href="#hexShape"/><g fill="none" stroke="#fff" stroke-width="2"><path d="M24 44l8-8 10 4 10-4 8 8M32 36l-4 12 12 10 6-4 4 2 6-8M40 46l6 6M44 44l6 6"/></g></svg>
  <p>Keine Verhandlungen mit<br>Lieferanten</p>
</div>
<div class="abs card" style="left:785px;top:1069px;width:284px;height:217px">
  <svg class="hex" viewBox="0 0 84 94"><use href="#hexShape"/><g fill="none" stroke="#fff" stroke-width="2"><path d="M32 28h16l8 8v30H32z"/><path d="M36 40h14M36 46h14M36 52h10M30 64l26-32"/></g></svg>
  <p>Keine Vertragsverpflichtung</p>
</div>

<h2 class="abs section-title interest">Hast du Interesse an einer Teilnahme?</h2>
<p class="abs lead">Dann trage dich gerne völlig unverbindlich in unsere Interessentenliste ein.</p>
<p class="abs intro">Um einen Eindruck von unseren Preisen zu erhalten schicken wir dir eine vorläufige<br>Preisliste zu und bitten dich um feedback. Welche Artikel interessieren dich? In welchen<br>Mengen benötigst du diese? Welche fehlen noch?</p>

<form class="abs form-card">
  <div class="field active" style="top:38px">First Name</div>
  <div class="field" style="top:86px">Last Name</div>
  <div class="field" style="top:134px">Email Address</div>
  <div class="field" style="top:182px;height:74px">Message</div>
  <span class="btn">ENQUIRE US</span>
</form>

<svg class="abs about" viewBox="0 0 1200 560" aria-hidden="true"><polygon points="0,12 1200,0 1200,560 0,560" fill="#ffffff"/></svg>

<div class="abs microscope" role="img" aria-label="Weißes Labormikroskop"></div>

<div class="abs feature" style="top:2182px">
  <svg width="52" height="52" viewBox="0 0 52 52" fill="none" stroke="#0e9bdc" stroke-width="2"><path d="M4 48h44M10 44V34M18 44V28M26 44V22M34 44V16M6 30L40 8M34 8h6v6"/><path d="M6 6h10M6 12h8M6 18h6" stroke="#0b3a6c"/></svg>
  <p><b>Unser Ziel</b> ist der Aufbau der ersten Einkaufsgemeinschaft für LifeScience Labore, über die jeder Teilnehmer seinen Laborbedarf zu Großhandelspreisen decken kann.</p>
</div>
<div class="abs feature" style="top:2270px">
  <svg width="52" height="52" viewBox="0 0 52 52" fill="none" stroke="#0e9bdc" stroke-width="2"><path d="M6 20h8l20-12v36L14 32H6z"/><path d="M10 32l4 12h6l-3-12"/><path d="M40 18l6-4M40 26h8M40 34l6 4" stroke="#0b3a6c"/></svg>
  <p><b>Das Kampagnenprinzip.</b> Wir bündeln euren Jahresbedarf an Chemikalien, Verbrauchsmaterialien und Laborbedarf und treten den Herstellern und Lieferanten gegenüber als ein starker Verhandlungspartner auf. Je mehr Teilnehmer mitmachen, desto größer wird unsere Verhandlungsmasse, desto besser unsere Einkaufspreise.</p>
</div>
<div class="abs feature" style="top:2428px">
  <svg width="52" height="52" viewBox="0 0 52 52" fill="none" stroke="#0e9bdc" stroke-width="2"><path d="M18 26V8a3 3 0 0 1 6 0v16l10 2a4 4 0 0 1 3 5l-3 12a4 4 0 0 1-4 3H22l-10-12a3 3 0 0 1 4-4l2 2"/></svg>
  <p><b>Keep it simple.</b> Wir verzichten auf Rahmenverträge, Mindestbestellmengen und sonstigen Verpflichtungen! Gefällt euch der ausgehandelte Preis, dann bezieht ihr ganz normal per Bestellung bei der Vessel Alliance euren Bedarf.</p>
</div>

<svg class="abs footer" viewBox="0 0 1200 190" aria-hidden="true"><polygon points="0,8 1200,60 1200,190 0,190" fill="#0b3a6c"/></svg>
<footer class="abs footer-text">Vessel Alliance e.K.<br>IMPRESSUM | DATENSCHUTZERKLÄRUNG</footer>

</body>
</html>
```